Dietary supplement, Clean and simple.

Hi,
I’d like to talk about the project,

About us:
We are a dietary supplement (Vitamins, Minerals, amino acids etc.) company.
The goal is to have about 25 products at the end of this year. However, for this goal to be achieved we need a good label design to make our products represent our company values.
I’ll be here every day supporting your questions, we are fully committed to making the highest/best quality/customer experience possible.

About the design and our values:
- Professional (We are in the industry of professionalism and expertise. I would love to show we are competent at this, Id. Like to have the labels looks like we have done our research.)
- Efficient (White spacing, good use of the space available.)
- Simple (Straight forward, in 5 seconds they have to know what the product they have is/how functions. We’re trying to simplify it for the consumer.
- No distractions (the only visually “distracting” factor can be the vector art.)

The guidelines:
The goal is to have a universal design, with one element that changes (Vector art). I’ll attach a file/multiple files I think can show some visuals on what I’m looking for, and what parts of the design I think are good/bad.

Label size: 69x155mm (Front is 77.5mm)

Design whatever you think fits our image. You’re the design expert, all I care about is that it fits our company standards/image.

Use this color/font.
Font: Sans Serif
Main company color is Mind green #237D62 (Use this color for something in the design.)

What I thought would be cool/might looks ugly, who knows:
1. The front of the label: Should have 1 vector art, preferably in the top right corner. (That looks good in multiple colors. The vector can have multiple areas to color, I would prefer 2 main colors in the vector art. The interchangeable colors are used for multiple kinds of products.)
2. Text/product information on the left. The text that will have to be displayed:
- Product name for instance “Magnesium + B6”
- Description for the product for instance “Magnesium with ginger taste”
- Company name or logo. (Add ® behind it. We are soon to be trademark registered.)
3. We need to show the "daily intake" amount on the front and also the amount in the complete bottle. For instance, “Daily intake 1 capsule, 60 capsules”.
• You don’t have to design the backside of the label. After I chose a design, I’d like to chat and give specific information on what areas need to be assigned where. (Too complex because of the law.)
Updates

Hi, Please make the deadline 31 days total. I want designers to have the time to design. And not be rushed to finish it.

I want to extend the deadline because i feel like a slightly more medical look would be interesting. Hope you can come up with something!!

Target Market(s)

Dietary supplement consumers

Industry/Entity Type

Dietary supplements

Font styles to use
Sans Serif

Colors

Designer to choose colors to be used in the design.

Requirements
Must have
• Trademark icon "®" has to be at the top right after the company logo(text of logo)/name.

```html
<!DOCTYPE html>
<html lang="en">
<head>
<meta charset="UTF-8">
<title>Verdant Calm – Magnesium + B6 Label</title>
<link href="https://fonts.googleapis.com/css2?family=Barlow:wght@300;400;600;700&display=swap" rel="stylesheet">
<style>
  :root {
    --backdrop: #bfcec1;
    --label-white: #f2f2f4;
    --mind-green: #237d62;
    --rule-green: #6aa892;
    --ink: #161616;
    --ink-soft: #2b2b2b;
    --art-blue: #9fd0f4;
    --art-sky: #7fb8f0;
    --art-violet: #8c86e0;
  }
  * { margin: 0; padding: 0; box-sizing: border-box; }
  html, body {
    width: 1200px;
    height: 1200px;
    overflow: hidden;
    background: var(--backdrop);
    font-family: "Barlow", sans-serif;
  }
  .canvas {
    position: relative;
    width: 1200px;
    height: 1200px;
  }
  .label-front {
    position: absolute;
    left: 220px;
    top: 122px;
    width: 760px;
    height: 956px;
    background: linear-gradient(90deg, #ffffff 0%, var(--label-white) 55%, #ececef 100%);
    overflow: hidden;
  }
  .vector-art {
    position: absolute;
    right: 0;
    top: 0;
    width: 342px;
    height: 434px;
    border-bottom-left-radius: 70% 55%;
    background:
      radial-gradient(ellipse at 70% 35%, var(--art-violet) 0%, rgba(140,134,224,0) 55%),
      linear-gradient(160deg, var(--art-sky) 0%, var(--art-blue) 70%, #c4e6fb 100%);
  }
  .accent-rule {
    position: absolute;
    left: 117px;
    top: 280px;
    width: 11px;
    height: 620px;
    background: var(--rule-green);
  }
  .brand {
    position: absolute;
    left: 158px;
    top: 418px;
    display: flex;
    align-items: center;
    gap: 16px;
    color: var(--mind-green);
    font-weight: 700;
    font-size: 58px;
    letter-spacing: 1px;
    text-transform: uppercase;
  }
  .brand-dot {
    width: 26px;
    height: 26px;
    border-radius: 50%;
    background: var(--mind-green);
  }
  .brand-name sup {
    font-size: 24px;
    vertical-align: top;
    position: relative;
    top: 4px;
    margin-left: 4px;
  }
  .product-name {
    position: absolute;
    left: 157px;
    top: 636px;
    font-size: 60px;
    font-weight: 600;
    color: var(--ink);
    letter-spacing: 0.5px;
  }
  .product-desc {
    position: absolute;
    left: 159px;
    top: 712px;
    font-size: 35px;
    font-weight: 300;
    color: var(--ink-soft);
    letter-spacing: 0.8px;
  }
  .dosage {
    position: absolute;
    left: 158px;
    top: 830px;
    font-size: 29px;
    font-weight: 400;
    color: var(--ink-soft);
    line-height: 50px;
    letter-spacing: 0.5px;
  }
</style>
</head>
<body>
<div class="canvas">
  <section class="label-front">
    <div class="vector-art" role="img" aria-label="Layered flowing petal vector art in blue and violet tones"></div>
    <div class="accent-rule"></div>
    <div class="brand">
      <span class="brand-dot"></span>
      <span class="brand-name">Verdant Calm<sup>®</sup></span>
    </div>
    <h1 class="product-name">MAGNESIUM + B6</h1>
    <p class="product-desc">Magnesium with Ginger Taste</p>
    <div class="dosage">
      <p>Daily Intake 1 Capsule</p>
      <p>60 Capsules</p>
    </div>
  </section>
</div>
</body>
</html>
```